Beekeeper needs a label for honey jars

Ciao! I'm from Como Italy
I'm a hobbyist beekeeper and I produce honey for myself and my friends.
I've named my apiary "Dado di sole," a play on words between my nickname (Dado, from Edoardo) and the Italian expression "Dado di sole," which translates to "a drizzle of honey" in English.
I need to create a label for my honey glass jars (250 gr and 500 gr).
I don't need a label for commercial purposes. I would like to include at least the name “Apicoltura Dado di sole", the type of honey (e.g., wildflower, acacia...) and a space for the production year, to be handwritten each year.
In the design some references to the world of bees.
For reference, attached a label with a style I like
Attached are the images of the selected jars and their measurements
Thanks and good job!

beekeeping, honey

• I would like an elegant style with clean graphics.
• Predominance of black color.

```html
<!DOCTYPE html>
<html lang="it">
<head>
<meta charset="utf-8">
<title>Apicoltura Dado di sole — Etichetta miele 250 g</title>
<link rel="stylesheet" href="https://fonts.googleapis.com/css2?family=Libre+Baskerville&family=Montserrat:wght@400;500&display=swap">
<style>
  :root {
    --bg: #ffffff;
    --label: #f1f1f1;
    --label-light: #fafafa;
    --flap-dark: #d6d6d6;
    --ink: #111111;
    --ink-soft: #333333;
    --rule: #9a9a9a;
    --comb: #e4e4e4;
    --flag-green: #2f8a3e;
    --flag-white: #ffffff;
    --flag-red: #d2262b;
  }
  html, body {
    margin: 0;
    width: 1200px;
    height: 1200px;
    overflow: hidden;
    background: var(--bg);
  }
  .canvas {
    position: relative;
    width: 1200px;
    height: 1200px;
  }
  .label {
    position: absolute;
    left: 100px;
    top: 270px;
    width: 1000px;
    height: 660px;
    background: linear-gradient(90deg, var(--label) 0%, var(--label-light) 50%, var(--label) 100%);
    border: 1px solid #cfcfcf;
    box-sizing: border-box;
    overflow: hidden;
  }
  .flap {
    position: absolute;
    top: 0;
    width: 90px;
    height: 100%;
  }
  .flap--left { left: 0; background: linear-gradient(90deg, var(--label-light), var(--flap-dark)); }
  .flap--right { right: 0; background: linear-gradient(90deg, var(--flap-dark), var(--label-light)); }
  .comb {
    position: absolute;
    background: var(--comb);
    opacity: .8;
  }
  .comb--top { left: 10px; top: 0; width: 480px; height: 220px; border-bottom-right-radius: 140px; }
  .comb--bottom { right: 0; bottom: 0; width: 480px; height: 220px; border-top-left-radius: 140px; }
  .since {
    position: absolute;
    top: 128px;
    left: 0;
    width: 100%;
    display: flex;
    justify-content: center;
    align-items: center;
    gap: 22px;
    font-family: "Montserrat", sans-serif;
    font-size: 14px;
    letter-spacing: 6px;
    color: var(--ink-soft);
  }
  .bee {
    width: 90px;
    height: 64px;
    background: radial-gradient(ellipse at center, #cfcfcf 0%, #e9e9e9 60%, transparent 72%);
  }
  .flag {
    position: absolute;
    top: 200px;
    left: 471px;
  }
  .text {
    position: absolute;
    left: 0;
    width: 100%;
    text-align: center;
    margin: 0;
    color: var(--ink);
  }
  .kicker {
    top: 242px;
    font-family: "Montserrat", sans-serif;
    font-weight: 500;
    font-size: 18px;
    letter-spacing: 4px;
  }
  .brand {
    top: 290px;
    font-family: "Libre Baskerville", serif;
    font-weight: 400;
    font-size: 74px;
    line-height: 1;
    letter-spacing: 1px;
  }
  .variety {
    top: 410px;
    font-family: "Montserrat", sans-serif;
    font-weight: 500;
    font-size: 18px;
    letter-spacing: 4px;
  }
  .divider {
    position: absolute;
    top: 460px;
    left: 480px;
    width: 40px;
    height: 2px;
    background: var(--ink);
  }
  .year {
    top: 503px;
    font-family: "Montserrat", sans-serif;
    font-size: 11px;
    letter-spacing: 5px;
  }
  .year-line {
    position: absolute;
    top: 556px;
    left: 372px;
    width: 266px;
    height: 1px;
    background: var(--rule);
  }
  .weight {
    top: 576px;
    font-family: "Montserrat", sans-serif;
    font-size: 14px;
    letter-spacing: 2px;
  }
</style>
</head>
<body>
<main class="canvas">
  <section class="label" aria-label="Etichetta vasetto miele 250 g">
    <div class="flap flap--left"></div>
    <div class="flap flap--right"></div>
    <div class="comb comb--top" role="img" aria-label="Motivo decorativo a nido d'ape, in alto a sinistra"></div>
    <div class="comb comb--bottom" role="img" aria-label="Motivo decorativo a nido d'ape, in basso a destra"></div>

    <div class="since">
      <span>SICE</span>
      <span class="bee" role="img" aria-label="Illustrazione di un'ape"></span>
      <span>2023</span>
    </div>

    <svg class="flag" width="58" height="8" viewBox="0 0 58 8" aria-label="Bandiera italiana">
      <rect x="0" y="0" width="19.3" height="8" fill="var(--flag-green)"/>
      <rect x="19.3" y="0" width="19.4" height="8" fill="var(--flag-white)"/>
      <rect x="38.7" y="0" width="19.3" height="8" fill="var(--flag-red)"/>
    </svg>

    <p class="text kicker">APICOLTURA</p>
    <h1 class="text brand">DADO DI SOLE</h1>
    <p class="text variety">WILDFLOWER HONEY</p>
    <div class="divider"></div>
    <p class="text year">PRODUCTION YEAR</p>
    <div class="year-line"></div>
    <p class="text weight">250 Gr</p>
  </section>
</main>
</body>
</html>
```